Flyer for the teaching seminar on prayer

I need a creative, but attractive and professional flyer made for an up coming church event.

Here is the content I would like to have on the Flyer:

The name of the event: Lamplight Assembly
Speaker: Bishop Adewunmi Kalunde
Speakers photo: <See attachement>
Date and Time:
Friday March 29th - 7:00 PM to 9:00 PM
Saturday Marche 30th - 7:00 PM to 9:00 PM
Sunday March 31st - 10:00 AM to 12:30 PM
Location:
Vaillant Community Center
418 Dunmore Lane, Portland, ME 04102
Welcome to TELVO, where the river meets the shore.

```html
<!DOCTYPE html>
<html lang="en">
<head>
<meta charset="utf-8">
<title>Lamplight Assembly — Flyer</title>
<link rel="stylesheet" href="https://fonts.googleapis.com/css2?family=Crimson+Text:wght@400;600;700&family=Arimo:wght@700&display=swap">
<style>
  :root {
    --navy: #06375e;
    --orange: #f29a2e;
    --orange-deep: #e58f26;
    --backdrop: #333333;
    --white: #ffffff;
  }
  * { box-sizing: border-box; margin: 0; padding: 0; }
  html, body { width: 1200px; height: 1200px; overflow: hidden; }
  body { background: var(--backdrop); position: relative; }

  .flyer {
    position: absolute; left: 242px; top: 112px;
    width: 708px; height: 1000px;
    overflow: hidden;
    box-shadow: 0 14px 40px rgba(0,0,0,.45);
  }
  .flyer__shapes { position: absolute; inset: 0; }

  .brand-name {
    position: absolute; left: 24px; top: 400px;
    font-family: "Crimson Text", serif; font-weight: 400;
    font-size: 62px; line-height: 1; letter-spacing: 1px;
    color: var(--white);
  }

  .event-title {
    position: absolute; left: 22px; top: 494px;
    font-family: "Crimson Text", serif; font-weight: 700;
    font-size: 62px; line-height: 64px; color: var(--white);
    text-transform: uppercase;
  }

  .speaker-band {
    position: absolute; left: 0; top: 658px; width: 436px; height: 34px;
    background: var(--orange); color: var(--white);
    font-family: "Arimo", sans-serif; font-weight: 700; font-size: 21px;
    line-height: 34px; padding-left: 22px; white-space: nowrap;
  }

  .speaker-photo {
    position: absolute; left: 434px; top: 558px; width: 220px; height: 220px;
    border-radius: 50%; border: 4px solid var(--orange);
    background: radial-gradient(circle at 50% 40%, #6c7a4a 0%, #3f5a8a 60%, #27407a 100%);
  }

  .schedule { position: absolute; left: 22px; top: 718px; }
  .schedule__label {
    display: inline-block; background: var(--orange); color: var(--white);
    font-family: "Crimson Text", serif; font-weight: 600; font-size: 19px;
    line-height: 24px; padding: 0 8px; border-radius: 12px;
  }
  .schedule__list {
    list-style: none; margin: 10px 0 0 6px;
    font-family: "Crimson Text", serif; font-size: 22.5px; line-height: 28.5px;
    color: var(--white); white-space: nowrap;
  }

  .welcome {
    position: absolute; left: 20px; top: 870px; width: 462px; height: 34px;
    background: var(--orange); border-radius: 17px; color: var(--white);
    font-family: "Arimo", sans-serif; font-weight: 700; font-size: 17.5px;
    line-height: 34px; text-align: center; white-space: nowrap;
  }

  .venue { position: absolute; left: 38px; top: 928px; display: flex; gap: 16px; color: var(--white); }
  .venue__pin { width: 18px; height: 26px; margin-top: 4px; }
  .venue__text {
    font-family: "Arimo", sans-serif; font-weight: 700; font-size: 16px; line-height: 20px;
  }
</style>
</head>
<body>
  <div class="flyer">
    <svg class="flyer__shapes" width="708" height="1000" viewBox="0 0 708 1000">
      <defs>
        <linearGradient id="crowdTone" x1="0" y1="0" x2="0.3" y2="1">
          <stop offset="0" stop-color="#3d4a50"/>
          <stop offset="0.45" stop-color="#4c5a66"/>
          <stop offset="1" stop-color="#1f2a38"/>
        </linearGradient>
      </defs>
      <rect class="crowd-photo" role="img" aria-label="Photo of a worship audience with raised hands facing a speaker on stage" width="708" height="1000" fill="url(#crowdTone)"/>
      <polygon class="corner-top" points="0,0 332,0 0,328" fill="var(--orange)"/>
      <polygon class="corner-top-shade" points="0,0 95,0 0,328" fill="var(--orange-deep)"/>
      <polygon class="panel-navy" points="0,328 122,216 550,1000 0,1000" fill="var(--navy)"/>
      <polygon class="corner-bottom" points="708,752 494,896 556,1000 708,1000" fill="var(--orange)"/>
    </svg>

    <div class="brand-name">TELVO</div>

    <h1 class="event-title">Lamplight<br>Assembly</h1>

    <div class="speaker-band">Speaker : Bishop Adewunmi Kalunde</div>

    <div class="speaker-photo" role="img" aria-label="Portrait of the speaker holding a microphone"></div>

    <div class="schedule">
      <span class="schedule__label">Date and Time :</span>
      <ul class="schedule__list">
        <li>Friday March 29th - 7:00 PM to 9:00 PM</li>
        <li>Saturday Marche 30th - 7:00 PM to 9:00 PM</li>
        <li>Sunday March 31st - 10:00 AM to 12:30 PM</li>
      </ul>
    </div>

    <div class="welcome">Welcome to TELVO, where the river meets the shore.</div>

    <div class="venue">
      <svg class="venue__pin" viewBox="0 0 18 26" aria-hidden="true">
        <path d="M9 0C4 0 0 4 0 9c0 6.5 9 17 9 17s9-10.5 9-17c0-5-4-9-9-9z" fill="var(--orange)"/>
        <circle cx="9" cy="9" r="3.5" fill="var(--navy)"/>
      </svg>
      <div class="venue__text">
        Vaillant Community Center<br>
        418 Dunmore Lane, Portland, ME 04102
      </div>
    </div>
  </div>
</body>
</html>
```